Company Business Card Design Project - Revamp the image of an old construction company.

We need a business card designed for a new company in Australia.

Type of business is Commercial Roofing & Painting.

Medium will be brushed black metal card that can/will be acid etched to a brushed steel silver, acid die cut and two printed colours of our choice which will be white and pantone orange.

We have hopes that the design will be simple, modern and represent with a quick glance what our company does.

Please read instructions carefully in must have box any questions please ask.

If you are interested in this job please look at other job that we have which is very similar with logo and design

Please have a look at the things that can be done with metals cards on yondle images for inspiration.

Target Market(s)

Business owners, commercial property development Men from 25-70 years of age.

Industry/Entity Type

Construction

Requirements
Must have
• Front of card:

Must use the company logo and name provided as attachment (see below kestrel mark construction_black_background).

the words -Commercial Painting and Roofing- must be on front of card

details needed on front or back depending on your design

Name
position
email
mobile

all details can be on front with a cool design to be etched on the back of card or to keep front simple you can put all detail on back of card, I will leave the lay out to you.

Colours in logo are

Pantone 144 C Orange
Pantone 11-0601 White
Pantone 7539 C Gray
Pantone 426 C Black

However black will be the base of black metal card. Gray will be replaced with the etching in card revealing the silver. Orange and white will be printed on card.

Please have fun!!
Should not have
• Please don't clutter the card
No fonts smaller then 7 points

```html
<!DOCTYPE html>
<html lang="en">
<head>
<meta charset="utf-8">
<title>Kestrel Mark Construction – Business Card</title>
<link href="https://fonts.googleapis.com/css2?family=Quicksand:wght@500;600;700&display=swap" rel="stylesheet">
<style>
  :root {
    --backdrop: #2b2b2c;
    --card-black: #1e2023;
    --card-edge: #34373b;
    --print-orange: #f7941d;
    --print-white: #e9e9e9;
    --etch-silver: #a7a9ac;
    --etch-dark: #16181a;
  }
  * { margin: 0; padding: 0; box-sizing: border-box; }
  html, body {
    width: 1200px;
    height: 1006px;
    overflow: hidden;
    background: var(--backdrop);
    font-family: "Quicksand", sans-serif;
  }
  .business-card {
    position: absolute;
    left: 100px;
    top: 188px;
    width: 1000px;
    height: 630px;
    background: var(--card-black);
    border: 1px solid var(--card-edge);
    border-radius: 26px;
    color: var(--print-white);
  }
  .brand {
    position: absolute;
    left: 70px;
    top: 70px;
    display: flex;
    align-items: center;
    gap: 18px;
  }
  .brand-square {
    width: 56px;
    height: 56px;
    background: var(--etch-silver);
  }
  .brand-name {
    font-weight: 700;
    font-size: 50px;
    line-height: 1;
    color: var(--print-orange);
    letter-spacing: 1px;
  }
  .brand-rule {
    position: absolute;
    left: 144px;
    top: 150px;
    width: 590px;
    height: 2px;
    background: var(--etch-silver);
  }
  .tagline {
    position: absolute;
    left: 144px;
    top: 168px;
    font-weight: 600;
    font-size: 30px;
    color: var(--etch-silver);
  }
  .etched-motif {
    position: absolute;
    right: 50px;
    top: 210px;
    width: 180px;
    height: 250px;
    background: var(--etch-dark);
    border-radius: 4px;
  }
  .holder-name {
    position: absolute;
    left: 70px;
    top: 300px;
    font-weight: 600;
    font-size: 42px;
    color: var(--etch-silver);
  }
  .holder-position {
    position: absolute;
    left: 70px;
    top: 362px;
    font-weight: 600;
    font-size: 28px;
    color: var(--etch-silver);
  }
  .contact-list {
    position: absolute;
    left: 70px;
    top: 430px;
    list-style: none;
  }
  .contact-item {
    display: flex;
    align-items: center;
    gap: 16px;
    height: 50px;
    font-weight: 600;
    font-size: 29px;
    color: var(--print-white);
    letter-spacing: 0.5px;
  }
  .contact-icon { width: 34px; height: 34px; flex: none; }
  .contact-icon * { fill: none; stroke: var(--etch-silver); stroke-width: 2; }
</style>
</head>
<body>
  <article class="business-card">
    <div class="brand">
      <span class="brand-square"></span>
      <span class="brand-name">KESTREL MARK CONSTRUCTION</span>
    </div>
    <div class="brand-rule"></div>
    <p class="tagline">Commercial Painting and Roofing</p>

    <div class="etched-motif" role="img" aria-label="Perforated etched brand motif"></div>

    <h1 class="holder-name">Your name</h1>
    <p class="holder-position">Position</p>

    <ul class="contact-list">
      <li class="contact-item">
        <svg class="contact-icon" viewBox="0 0 34 34" aria-hidden="true">
          <rect x="10" y="3" width="14" height="28" rx="3"/>
          <line x1="15" y1="27" x2="19" y2="27"/>
        </svg>
        (012) 555 - 6789
      </li>
      <li class="contact-item">
        <svg class="contact-icon" viewBox="0 0 34 34" aria-hidden="true">
          <rect x="3" y="8" width="28" height="19" rx="1"/>
          <polyline points="3,8 17,19 31,8"/>
        </svg>
        yourname@kestrelmark.com
      </li>
      <li class="contact-item">
        <svg class="contact-icon" viewBox="0 0 34 34" aria-hidden="true">
          <circle cx="17" cy="17" r="13"/>
          <ellipse cx="17" cy="17" rx="6" ry="13"/>
          <line x1="4" y1="17" x2="30" y2="17"/>
          <line x1="7" y1="10" x2="27" y2="10"/>
          <line x1="7" y1="24" x2="27" y2="24"/>
        </svg>
        www.kestrelmark.com
      </li>
    </ul>
  </article>
</body>
</html>
```